Marlow Family Chiropractic Stationary

The letterhead and business card must have our logo.
We would like to see the logo used in different ways ( It can be expanded upon in the stationary.)
Please use the the same or similar colors.
Must be eye catching and memorable.
Must be easy to read

Reason: The doctor has been too busy to make any final decisions. He would like to give himself a little more time.

Target Market(s)

Chiropractic Healthcare

Industry/Entity Type

Business

Requirements
Must have
• Dr. Nathaniel Marlow D.C.
Chiropractor

555-555-0193

415 Birchwood Parkway, Suite 200
Ashbrook, ST 00199

drmarlow@marlowspine.example
www.marlowspine.example
www.facebook.com/MarlowFamilySpine
Should not have
• should not be difficult to read

```html
<!DOCTYPE html>
<html lang="en">
<head>
<meta charset="utf-8">
<title>Marlow Family Chiropractic – Business Card</title>
<link rel="stylesheet" href="https://fonts.googleapis.com/css2?family=PT+Sans:wght@400;700&display=swap">
<style>
  :root {
    --bg: #e6e9eb;
    --card: #ffffff;
    --ink: #3a3a3a;
    --green: #3a9a2e;
    --green-dark: #2f8a24;
    --lime: #a8cf3a;
    --yellow: #e8e000;
    --olive: #b8a500;
    --faint: #eeeeee;
  }
  * { box-sizing: border-box; margin: 0; padding: 0; }
  html, body { width: 1200px; height: 960px; overflow: hidden; }
  body {
    background: var(--bg);
    font-family: "PT Sans", Arial, sans-serif;
    color: var(--ink);
    display: flex;
    flex-direction: column;
    align-items: center;
    justify-content: center;
    gap: 48px;
  }
  .card {
    position: relative;
    width: 700px;
    height: 400px;
    background: var(--card);
    box-shadow: 0 6px 20px rgba(0,0,0,.12);
    overflow: hidden;
  }
  .card__band {
    position: absolute;
    left: 0; right: 0; bottom: 0;
    height: 22px;
    background: linear-gradient(90deg, var(--green) 0%, var(--lime) 40%, var(--yellow) 85%, var(--olive) 100%);
  }
  .card__decor {
    position: absolute;
    top: 0; bottom: 22px;
    width: 220px;
    background: radial-gradient(ellipse at center, var(--faint) 0%, rgba(238,238,238,0) 70%);
  }

  /* Contact side */
  .card--contact .card__decor { left: 0; }
  .brand-mark {
    position: absolute;
    left: 50px; top: 100px;
    width: 230px;
    display: flex;
    flex-direction: column;
    align-items: center;
    gap: 14px;
    text-align: center;
  }
  .brand-mark__dot {
    width: 110px; height: 110px;
    border-radius: 50%;
    background: var(--green);
  }
  .brand-mark__name {
    font-weight: 700;
    font-size: 20px;
    line-height: 1.2;
    color: var(--green);
  }
  .details {
    position: absolute;
    left: 320px; top: 66px;
    width: 340px;
  }
  .details__name { font-size: 27px; font-weight: 400; color: var(--ink); line-height: 1.2; }
  .details__title {
    font-size: 16px;
    letter-spacing: .5px;
    text-transform: uppercase;
    padding-bottom: 6px;
    border-bottom: 2px solid var(--green);
    margin-bottom: 22px;
  }
  .contact-list { list-style: none; display: grid; gap: 7px; }
  .contact-list li { display: flex; align-items: center; gap: 12px; font-size: 17px; }
  .contact-list svg { width: 16px; height: 16px; flex: none; }
  .details__address { margin-top: 26px; font-size: 18px; line-height: 1.3; font-style: normal; }

  /* Brand side */
  .card--brand .card__decor { right: 0; }
  .brand-lockup {
    position: absolute;
    left: 0; right: 0; top: 60px;
    display: flex;
    flex-direction: column;
    align-items: center;
    gap: 18px;
    text-align: center;
  }
  .brand-lockup__dot {
    width: 150px; height: 150px;
    border-radius: 50%;
    background: var(--green);
  }
  .brand-lockup__name {
    font-weight: 700;
    font-size: 36px;
    line-height: 1.1;
    letter-spacing: 1px;
    text-transform: uppercase;
    color: var(--green-dark);
  }
</style>
</head>
<body>

  <section class="card card--contact">
    <div class="card__decor" role="img" aria-label="Faint scattered leaf background motif"></div>
    <div class="brand-mark">
      <span class="brand-mark__dot"></span>
      <span class="brand-mark__name">Marlow Family Chiropractic</span>
    </div>
    <div class="details">
      <h1 class="details__name">Dr. Nathaniel Marlow D.C.</h1>
      <p class="details__title">Chiropractor</p>
      <ul class="contact-list">
        <li>
          <svg viewBox="0 0 16 16" aria-hidden="true"><rect x="3" y="1" width="10" height="14" rx="1.5" fill="none" stroke="var(--green)" stroke-width="1.5"/><line x1="6" y1="12" x2="10" y2="12" stroke="var(--green)" stroke-width="1.5"/></svg>
          555-555-0193
        </li>
        <li>
          <svg viewBox="0 0 16 16" aria-hidden="true"><rect x="1" y="3" width="14" height="10" fill="none" stroke="var(--green)" stroke-width="1.3"/><polyline points="1,3 8,9 15,3" fill="none" stroke="var(--green)" stroke-width="1.3"/></svg>
          drmarlow@marlowspine.example
        </li>
        <li>
          <svg viewBox="0 0 16 16" aria-hidden="true"><rect x="2" y="2" width="12" height="12" rx="2" fill="var(--green)"/></svg>
          /MarlowFamilySpine
        </li>
        <li>
          <svg viewBox="0 0 16 16" aria-hidden="true"><circle cx="8" cy="8" r="6.5" fill="none" stroke="var(--green)" stroke-width="1.4"/><ellipse cx="8" cy="8" rx="2.8" ry="6.5" fill="none" stroke="var(--green)" stroke-width="1.1"/><line x1="1.5" y1="8" x2="14.5" y2="8" stroke="var(--green)" stroke-width="1.1"/></svg>
          www.marlowspine.example
        </li>
      </ul>
      <address class="details__address">415 Birchwood Parkway, Suite 200<br>Ashbrook, ST 00199</address>
    </div>
    <div class="card__band"></div>
  </section>

  <section class="card card--brand">
    <div class="card__decor" role="img" aria-label="Faint scattered leaf background motif"></div>
    <div class="brand-lockup">
      <span class="brand-lockup__dot"></span>
      <span class="brand-lockup__name">Marlow Family<br>Chiropractic</span>
    </div>
    <div class="card__band"></div>
  </section>

</body>
</html>
```